Etiketten-Design für eine recycelte Flagge gesucht
Zielgruppe
Wir bieten Länderfahnen z.B. Deutschland Flaggen usw. an. In diesem Fall geht es um recycelte Flagge - das Material wird aus alten Plastikflaschen gewonnen
Aufgabenstellung
Etikett für eine recycelte Flagge
Das Etikett wird für mehrere verschiedene Designs verwendet, daher hier nur als Beispiel die Deutschland Flagge.
Größe: 12x6cm
Druckart: Digitaldruck
Druckdatei: pdf
folgende Infos müssen enthalten sein:
(Beispielhaft an der Deutschland Flagge)
Name: Deutschland Flagge in recycelter Premium Qualität
Artikelnummer: 372
EAN Code: 4251938407561
Material: Polyester recycelt
Größe: 90 x 150 cm
(wenn möglich => Grafische Darstellung der Deutschland Flagge - KEIN FOTO)
Logo: siehe Dateien
Anschrift:
velumor GmbH
Am Hang 8
79346 Talbrunn - Germany
info@velumor.com
URL des Shops: www.quiro-banner.com
Das Etikett wird auf einer braunen Papiertüte angebracht.

```html
<!DOCTYPE html>
<html lang="de">
<head>
<meta charset="utf-8">
<title>Deutschland Flagge – Etikett</title>
<link href="https://fonts.googleapis.com/css2?family=Jost:wght@300;400;500&family=Saira+Semi+Condensed:wght@800&display=swap" rel="stylesheet">
<style>
  :root {
    --band-grey: #808488;
    --ink: #1d1d1b;
    --paper: #ffffff;
    --flag-black: #1d1d1b;
    --flag-red: #cd1719;
    --flag-gold: #ffed00;
  }
  * { margin: 0; padding: 0; box-sizing: border-box; }
  html, body { width: 1200px; height: 600px; overflow: hidden; background: var(--paper); }
  .label {
    position: relative;
    width: 1200px;
    height: 600px;
    background: var(--paper);
    overflow: hidden;
    font-family: "Jost", "Futura", sans-serif;
    color: var(--ink);
  }
  .header-band {
    position: absolute;
    inset: 0 0 auto 0;
    height: 352px;
    background: var(--band-grey);
  }
  .flag-stripes {
    position: absolute;
    inset: 0;
    width: 1200px;
    height: 600px;
  }
  .brand {
    position: absolute;
    left: 44px;
    top: 78px;
    display: flex;
    align-items: center;
    gap: 12px;
    font-weight: 500;
    font-size: 28px;
    letter-spacing: 1px;
    line-height: 32px;
    color: var(--ink);
  }
  .brand-dot {
    width: 24px;
    height: 24px;
    border-radius: 50%;
    background: var(--ink);
    flex: none;
  }
  .product-title {
    position: absolute;
    left: 296px;
    top: 40px;
    width: 600px;
    height: 200px;
  }
  .product-title text {
    font-family: "Saira Semi Condensed", "Arial Narrow", sans-serif;
    font-weight: 800;
    font-size: 104px;
    fill: var(--ink);
  }
  .quality {
    position: absolute;
    left: 305px;
    top: 244px;
    display: flex;
    align-items: center;
    gap: 14px;
  }
  .recycle-icon { width: 86px; height: 84px; flex: none; }
  .quality-text {
    font-weight: 300;
    font-size: 36px;
    line-height: 38px;
    text-transform: uppercase;
  }
  .code-frame {
    position: absolute;
    left: 31px;
    top: 366px;
    width: 370px;
    height: 212px;
    border: 3px solid var(--ink);
    background: var(--paper);
    display: flex;
    align-items: flex-end;
    justify-content: center;
    padding-bottom: 14px;
  }
  .ean {
    font-size: 22px;
    letter-spacing: 2px;
  }
  .product-info {
    position: absolute;
    left: 422px;
    top: 364px;
    font-size: 23px;
    line-height: 28px;
    font-weight: 400;
  }
  .maker-info { margin-top: 16px; }
</style>
</head>
<body>
<main class="label">
  <div class="header-band"></div>

  <svg class="flag-stripes" viewBox="0 0 1416 709" preserveAspectRatio="none" aria-hidden="true">
    <polygon points="880,243 1386,0 1416,0 1416,240 983,448" fill="var(--flag-black)"/>
    <polygon points="983,448 1416,240 1416,491 1080,652" fill="var(--flag-red)"/>
    <polygon points="1080,652 1416,491 1416,709 1106,709" fill="var(--flag-gold)"/>
  </svg>

  <div class="brand"><span class="brand-dot"></span><span>QUIRO<br>BANNER</span></div>

  <svg class="product-title" viewBox="0 0 600 200" role="heading" aria-level="1" aria-label="Deutschland Flagge">
    <text x="2" y="85" textLength="588" lengthAdjust="spacingAndGlyphs">DEUTSCHLAND</text>
    <text x="2" y="191" textLength="310" lengthAdjust="spacingAndGlyphs">FLAGGE</text>
  </svg>

  <div class="quality">
    <svg class="recycle-icon" viewBox="0 0 100 96" aria-hidden="true">
      <g fill="var(--ink)">
        <path d="M38 6 L62 6 L74 27 L82 22 L76 46 L54 40 L62 35 L52 18 L40 38 L22 28 Z"/>
        <path d="M88 56 L98 74 L86 94 L62 94 L62 104 L46 84 L62 66 L62 76 L80 76 L70 58 Z" transform="translate(0,-10)"/>
        <path d="M10 46 L2 62 L14 84 L38 84 L38 66 L22 66 L30 52 L38 57 L30 32 L8 40 Z"/>
      </g>
    </svg>
    <p class="quality-text">Recycelte Premium<br>Qualität</p>
  </div>

  <div class="code-frame"><span class="ean">EAN 4251938407561</span></div>

  <section class="product-info">
    <p>Artikel Nummer: 372<br>Größe: 90 x 150 cm<br>Material: Polyester recycelt</p>
    <p class="maker-info">velumor GmbH - Am Hang 8<br>79346 Talbrunn - Germany<br>info@velumor.com - www.quiro-banner.com</p>
  </section>
</main>
</body>
</html>
```